Financial Advisor Brochure to attract new clients

I am launching a new career as a Financial Advisor and a flier that shows what services I offer and why I decided to go back to work at this point in my life. I have a deep desire to help people meet their dreams and believe that a solid financial foundation provides the ability to live your life as you want to and not how you have to. I created a simple flier but know that so much more can be done to catch a persons eye.

Target Market(s)

Entrepeneurs and Woman in all stages of life.

Industry/Entity Type

Financial Advisor

Font styles to use
Sans Serif

Colors
00AB8E
00BBA5
67D7C9
C6EFE9
E9F9F6

Requirements
Must have
• my photo, contact information and Tessaly Logo

```html
<!DOCTYPE html>
<html lang="en">
<head>
<meta charset="utf-8">
<title>Marla Devereux – Financial Advisor Profile</title>
<link href="https://fonts.googleapis.com/css2?family=Raleway:wght@400;500;600;700;800&display=swap" rel="stylesheet">
<style>
:root{
  --page-bg:#e9e9e9;
  --brand-blue:#0b6fb8;
  --brand-blue-deep:#085a9a;
  --pill-blue:#3ea3ee;
  --accent-blue:#1b6fb4;
  --panel-grey:#ededed;
  --footer-grey:#7b7878;
  --ink:#2a2a2a;
  --white:#ffffff;
}
*{margin:0;padding:0;box-sizing:border-box}
html,body{width:718px;height:1200px;overflow:hidden}
body{background:var(--page-bg);font-family:"Raleway",sans-serif;color:var(--ink);position:relative}
.flyer{position:absolute;left:0;top:136px;width:718px;height:928px;background:var(--white);overflow:hidden;box-shadow:0 6px 20px rgba(0,0,0,.18)}
.hero{position:absolute;left:0;top:0;width:718px;height:320px;background:linear-gradient(135deg,var(--brand-blue) 0%,var(--brand-blue-deep) 100%)}
.hero-name{position:absolute;left:49px;top:46px;color:var(--white);font-weight:800;font-size:27px;letter-spacing:.2px}
.hero-role{position:absolute;left:49px;top:82px;color:var(--white);font-weight:400;font-size:24px}
.profile-pill{position:absolute;left:49px;top:127px;width:199px;height:36px;border-radius:18px;background:var(--pill-blue);color:#0d2a4a;font-weight:500;font-size:26px;line-height:36px;padding-left:14px}
.hero-tagline{position:absolute;left:50px;top:184px;width:320px;color:var(--white);font-weight:500;font-size:18px;line-height:22px}
.portrait{position:absolute;left:391px;top:14px;width:262px;height:306px;background:radial-gradient(ellipse at 50% 30%,#8a5a3c 0%,#5e3a28 30%,#1e8f78 60%,#0b6fb8 85%);border-radius:40% 40% 0 0}
.about{position:absolute;left:0;top:320px;width:718px;height:225px}
.about-left{position:absolute;left:0;top:0;width:383px;height:158px;background:var(--panel-grey)}
.about-right{position:absolute;left:383px;top:0;width:335px;height:225px;background:var(--panel-grey);border-bottom-left-radius:14px}
.about p{font-size:9.6px;line-height:12.6px;margin-bottom:12px}
.about-left .copy{position:absolute;left:50px;top:16px;width:300px}
.about-right .copy{position:absolute;left:24px;top:14px;width:282px}
.services-title{position:absolute;left:50px;top:493px;font-size:20.5px;font-weight:500;line-height:25px}
.service{position:absolute}
.service h3{font-size:15px;font-weight:500;margin-bottom:9px}
.service h3 span{color:var(--accent-blue)}
.service ul{list-style:none}
.service li{font-size:9.8px;line-height:13px;position:relative;padding-left:15px;margin-bottom:2px}
.service li::before{content:"";position:absolute;left:0;top:3px;width:7px;height:7px;border-radius:50%;border:1px solid var(--pill-blue)}
.service-icon{position:absolute;width:40px;height:40px}
.footer-call{position:absolute;left:0;top:832px;width:440px;height:96px}
.call-label{position:absolute;left:52px;top:852px;color:var(--white);font-size:16px;font-weight:500;letter-spacing:.3px}
.call-number{position:absolute;left:93px;top:870px;color:var(--white);font-size:33px;font-weight:800;letter-spacing:.5px}
.call-icon{position:absolute;left:50px;top:880px}
.contact{position:absolute;left:0;top:0}
.contact-line{position:absolute;left:450px;color:var(--white);font-size:12.3px;font-weight:500}
.contact-icon{position:absolute;left:426px}
</style>
</head>
<body>
<main class="flyer">
  <section class="hero">
    <h1 class="hero-name">MARLA DEVEREUX</h1>
    <p class="hero-role">Financial Advisor</p>
    <div class="profile-pill">PROFILE</div>
    <p class="hero-tagline">Passionate about helping empower you with knowledge to make informed financial decisions throughout all of life’s stages and help you achieve your goals.</p>
    <div class="portrait" role="img" aria-label="Portrait photo of the financial advisor in a green blouse, smiling, leaning on a desk"></div>
  </section>

  <section class="about">
    <div class="about-left">
      <div class="copy">
        <p>As a business owner, wife, and mother of two teenagers, I understand the struggles you face juggling your personal, business, and financial life.</p>
        <p>I grew up in a home where my parents had opposing money habits. My Dad was a big spender and mom was a saver. Through the years, I saw how my mom’s consistent savings grew while Dad’s style led to many financial ups and downs. This made a huge impression on me and sparked my continued interest in all things finance.</p>
      </div>
    </div>
    <div class="about-right">
      <div class="copy">
        <p>Having an entrepreneurial personality and ability to explain concepts in a relatable manner has provided me with many opportunities. In 2018, After decades of running a sales agency, I sold my company to spend time with my kids and family but my interest in Finance never waned. Now that our kids are thriving teenagers, I started a new career as a licensed Financial Advisor with a heart to help you achieve your financial dreams.</p>
        <p>The financial world is changing rapidly, and it can be confusing on how to maneuver through these times. My goal is to pull out the emotions that cloud judgement and help you make better decisions with your long-range goals in mind.</p>
      </div>
    </div>
  </section>

  <h2 class="services-title">Financial planning services<br>offered:</h2>

  <svg class="service-icon" style="left:46px;top:556px" viewBox="0 0 40 40" fill="none" stroke="#333" stroke-width="1.6"><circle cx="20" cy="20" r="13"/><circle cx="20" cy="20" r="6"/><path d="M20 3v4M20 33v4M3 20h4M33 20h4"/></svg>
  <div class="service" style="left:110px;top:559px;width:230px">
    <h3>Transition <span>Planning</span></h3>
    <ul><li>Divorce planning.</li><li>Strategy and guidance pre, during, and post- divorce</li></ul>
  </div>

  <svg class="service-icon" style="left:46px;top:638px" viewBox="0 0 40 40" fill="none" stroke="#333" stroke-width="1.6"><circle cx="18" cy="10" r="5"/><path d="M8 18h26M12 18v18M8 36h16M18 22v14"/></svg>
  <div class="service" style="left:110px;top:642px;width:230px">
    <h3>Retirement <span>planning</span></h3>
    <ul><li>Current portfolio analysis</li><li>Timeline asset and income planning</li><li>Tax and estate review and projections</li></ul>
  </div>

  <svg class="service-icon" style="left:46px;top:736px" viewBox="0 0 40 40" fill="none" stroke="#333" stroke-width="1.6"><path d="M4 18L20 5l16 13M8 15v20h24V15"/><path d="M12 26l6 4 10-8"/></svg>
  <div class="service" style="left:110px;top:741px;width:240px">
    <h3>Real estate <span>acquisition or sale</span></h3>
    <ul><li>Acquisition or dissolution of real estate. Individual or portfolio</li></ul>
  </div>

  <svg class="service-icon" style="left:369px;top:562px" viewBox="0 0 40 40" fill="none" stroke="#333" stroke-width="1.6"><circle cx="20" cy="25" r="9"/><path d="M20 20v10M17 22h5M17 28h5M4 10l10 4M36 10l-10 4"/></svg>
  <div class="service" style="left:433px;top:566px;width:240px">
    <h3>Business <span>sale or purchase</span></h3>
    <ul><li>Company valuations</li><li>Tax impact analysis</li><li>Strategy implementation for funds received from sale</li></ul>
  </div>

  <svg class="service-icon" style="left:369px;top:662px" viewBox="0 0 40 40" fill="none" stroke="#333" stroke-width="1.6"><rect x="12" y="4" width="16" height="22"/><path d="M16 9h3M21 9h3M16 14h3M21 14h3M16 19h3M21 19h3M4 30l10 6h14l8-6"/></svg>
  <div class="service" style="left:433px;top:667px;width:240px">
    <h3>Estate <span>planning:</span></h3>
    <ul><li>Strategies for creating future generational wealth.</li></ul>
  </div>

  <svg class="service-icon" style="left:369px;top:742px" viewBox="0 0 40 40" fill="none" stroke="#333" stroke-width="1.6"><path d="M4 20v-8M8 20v-12M12 20v-6"/><circle cx="26" cy="10" r="5"/><path d="M18 34v-8c0-5 16-5 16 0v8"/><circle cx="8" cy="30" r="4"/></svg>
  <div class="service" style="left:433px;top:745px;width:240px">
    <h3>New <span>Investors:</span></h3>
    <ul><li>Assistance in opening investment and retirement acc</li></ul>
  </div>

  <svg class="contact" width="718" height="928" viewBox="0 0 718 928" aria-hidden="true">
    <defs><linearGradient id="footerBlue" x1="0" x2="1"><stop offset="0" stop-color="#0b6fb8"/><stop offset="1" stop-color="#1f86d4"/></linearGradient></defs>
    <path d="M0 832H325c20 0 30 20 40 40c10 20 22 56 52 56H0Z" fill="#7b7878"/>
    <path d="M362 851H718V928H410c-20 0-26-30-48-77Z" fill="url(#footerBlue)"/>
  </svg>

  <p class="call-label">CALL FOR AN APPOINTMENT</p>
  <svg class="call-icon" width="30" height="30" viewBox="0 0 30 30" fill="none" stroke="#fff" stroke-width="1.8"><path d="M7 4l5 5-3 3c2 4 5 7 9 9l3-3 5 5-4 4C12 26 4 18 3 8Z"/><path d="M18 4a9 9 0 0 1 8 8M18 9a4 4 0 0 1 3 3"/></svg>
  <p class="call-number">555-214-0386</p>

  <svg class="contact-icon" style="top:891px" width="16" height="12" viewBox="0 0 16 12" fill="none" stroke="#fff" stroke-width="1.2"><rect x=".6" y=".6" width="14.8" height="10.8"/><path d="M.6.6L8 7 15.4.6"/></svg>
  <p class="contact-line" style="top:888px">marla.devereux@tessalywealthalliance.com</p>
  <svg class="contact-icon" style="top:911px" width="14" height="14" viewBox="0 0 14 14" fill="none" stroke="#fff" stroke-width="1.1"><circle cx="7" cy="7" r="6"/><ellipse cx="7" cy="7" rx="2.6" ry="6"/><path d="M1 7h12"/></svg>
  <p class="contact-line" style="top:909px">www.tessalywealthalliance.com</p>
</main>
</body>
</html>
```